Convention Display

We need a convention booth design for an 10' W x 8' T booth. It should match the look and feel of our website and our brochure design. Sample design and text via 'upload files' below. www.corvinbrook.com

```html
<!DOCTYPE html>
<html lang="en">
<head>
<meta charset="utf-8">
<title>Corvin Brook – Convention Booth</title>
<link href="https://fonts.googleapis.com/css2?family=Arimo:ital,wght@0,400;0,700;1,700&display=swap" rel="stylesheet">
<style>
  :root {
    --page-bg: #d6d7d8;
    --panel-white: #ffffff;
    --panel-grey: #e8e9ea;
    --label-strip: #eeeff0;
    --ink: #3a3f44;
    --ink-brand: #3d4b56;
    --green: #8dc63f;
    --blue: #1b6db3;
    --orange: #f0891d;
    --photo-light: #d4d4d4;
    --photo-dark: #8e8e8e;
  }
  html, body {
    margin: 0;
    width: 1200px;
    height: 624px;
    overflow: hidden;
    background: var(--page-bg);
    font-family: "Arimo", Arial, sans-serif;
  }
  .booth-panel {
    position: absolute;
    left: 200px;
    top: 17px;
    width: 800px;
    height: 590px;
    background: var(--panel-white);
    overflow: hidden;
  }
  .panel-art {
    position: absolute;
    inset: 0;
  }
  .brand-name {
    position: absolute;
    left: 36px;
    top: 24px;
    margin: 0;
    font-size: 38px;
    font-weight: 700;
    color: var(--ink-brand);
    letter-spacing: -0.5px;
  }
  .headline {
    position: absolute;
    right: 48px;
    top: 18px;
    margin: 0;
    text-align: right;
    font-weight: 700;
    color: var(--ink);
    line-height: 29px;
  }
  .headline .line-one { font-size: 20px; }
  .headline .line-two { font-size: 19px; }
  .headline .accent { color: var(--green); font-style: italic; }
  .step-label {
    position: absolute;
    top: 112px;
    margin: 0;
    font-size: 18px;
    color: var(--ink);
    white-space: nowrap;
  }
  .benefit-row {
    position: absolute;
    margin: 0;
    white-space: nowrap;
    font-size: 19px;
    display: flex;
    gap: 22px;
  }
  .benefit-row.bold { font-weight: 700; }
  .row-one { left: 35px; top: 391px; }
  .row-two { left: 188px; top: 420px; }
  .row-three { left: 79px; top: 449px; }
  .c-blue { color: var(--blue); }
  .c-green { color: var(--green); }
  .c-orange { color: var(--orange); }
  .approach {
    position: absolute;
    left: 44px;
    top: 500px;
    margin: 0;
    color: var(--ink);
  }
  .approach-title { display: block; font-size: 24px; font-style: italic; font-weight: 700; color: var(--green); }
  .approach-note { display: block; font-size: 12px; margin-top: 2px; }
  .approach-arrow { position: absolute; left: 216px; top: 508px; }
  .site-url {
    position: absolute;
    left: 345px;
    top: 528px;
    margin: 0;
    font-size: 31px;
    color: var(--ink);
  }
</style>
</head>
<body>
  <main class="booth-panel">
    <svg class="panel-art" width="800" height="590" viewBox="0 0 800 590">
      <defs>
        <linearGradient id="photoTone" x1="0" y1="0" x2="1" y2="1">
          <stop offset="0" stop-color="var(--photo-light)"/>
          <stop offset="1" stop-color="var(--photo-dark)"/>
        </linearGradient>
      </defs>
      <polygon class="header-band" points="380,0 800,0 800,93 348,93" fill="var(--panel-grey)"/>
      <rect class="rule" x="0" y="97" width="800" height="6" fill="var(--green)"/>
      <rect class="label-strip" x="0" y="103" width="800" height="40" fill="var(--label-strip)"/>
      <g role="img" aria-label="Photo: woman smiling and holding a tablet">
        <polygon points="0,143 258,143 216,374 0,374" fill="url(#photoTone)"/>
      </g>
      <g role="img" aria-label="Photo: older couple smiling at a laptop">
        <polygon points="265,143 491,143 461,374 223,374" fill="url(#photoTone)"/>
      </g>
      <g role="img" aria-label="Photo: young couple looking at a printed scan">
        <polygon points="498,143 800,143 800,374 468,374" fill="url(#photoTone)"/>
      </g>
      <polygon class="footer-band" points="310,484 800,484 800,590 271,590" fill="var(--panel-grey)"/>
    </svg>

    <h1 class="brand-name">corvin brook</h1>
    <h2 class="headline">
      <span class="line-one"><span class="accent">3 STEPS</span> TO ENGAGEMENT</span><br>
      <span class="line-two">A NEW GENERATION PATIENT PORTAL</span>
    </h2>

    <p class="step-label" style="left:20px">make it personal</p>
    <p class="step-label" style="left:305px">make it shared</p>
    <p class="step-label" style="left:565px">make it relevant</p>

    <p class="benefit-row bold row-one">
      <span class="c-blue">Improve satisfaction</span>
      <span class="c-orange">Integrate your PHR</span>
      <span class="c-green">Streamline care</span>
    </p>
    <p class="benefit-row row-two">
      <span class="c-green">Meet meaningful use</span>
      <span class="c-blue">Increase donations</span>
      <span class="c-orange">Incorporate staff</span>
    </p>
    <p class="benefit-row bold row-three">
      <span class="c-orange">Change behavior</span>
      <span class="c-green">Capture analytics</span>
      <span class="c-blue">Grow your community</span>
    </p>

    <p class="approach">
      <span class="approach-title">our approach</span>
      <span class="approach-note">learn more about our method</span>
    </p>
    <svg class="approach-arrow" width="22" height="14" viewBox="0 0 22 14" aria-hidden="true">
      <path d="M1 9 Q8 5 15 6" stroke="#6c7680" stroke-width="2.5" fill="none"/>
      <polygon points="14,1 21,6 14,11" fill="#6c7680"/>
    </svg>

    <p class="site-url">www.corvinbrook.com</p>
  </main>
</body>
</html>
```